Classical music image - Lanterns of Marrow Hollow

We are six musicians living in Australia and performing concerts in July 2016 including at Brinmoor Concert Hall. Almost all our music is very modern in a classical style, and this time around one piece is titled "Lanterns of Marrow Hollow". We want a mysterious, dark, musical image that will suit posters, flyers, and business cards. Other things to include are musical instruments and elements of mythology, dungeons, and the underworld.

We also need a website. It should be stylish, modern, and bright, showing our group as young, energetic, new musicians. It does not require much special functionality, it's more to give information and pictures and updates of our projects.

Target Market(s)

Classical music lovers, with a taste of modern art

Industry/Entity Type

House

Number of Pages Required

5+ page

Requirements
Must have
• For the poster - the concert is called "Lanterns of Marrow Hollow". Once we have the right image, those words will have to be added. We will also need space to add our logo, our group name, performers names, composers, dates and times of concerts.
• If you want photos for the poster, use those uploaded on 26 April. The names of those photos are Single PtR, Single KJ, Single TL, Single NF, Mira2.6846, Tobin.H&S, and Kulomi Smiling (4 people), Kulomi Serious (4 people).
• The image should be dark/mysterious/moody
• It should include a picture of clarinet, saxophone
• It might be scary
• It might include images that suggest a dungeon, the underworld, any gods or mythological creatures that might be found in the darkness
• It might show a musician journeying down a staircase, or through a dark tunnel
• There might be a creature hidden in the darkness
• For the website - the mood is totally different, we are a cheerful, modern group of young musicians, and we would like a stylish, simple and easy to use and read website. The colours of the group "Windlark" are silver, gold, white and black, but any colours are okay.
• We have plenty of photos of our group (uploaded on 21 April), The Windlark Ensemble, and logo designed already. We need (1) welcome page where news and events and updates appear; then we need (2) a page with a detailed listing of events; (3) a page of about this group; (4) a page of our biographies; and (5) a page of our past concerts; (6) a page of links to listen to our music; and (7) page of other links and a contact form.
• I should be able to easily update the website using Wordpress and Gigpress or something equally easy. I am okay at computers but I don't want to have to learn anything tricky, thank you!
• My current other site is tobinfarrowreeds.com to give you an idea or two.
Nice to have
• Poster
• It might also have an image of a flute
• Any other suggestions of music, such as musical symbols
• Website - silver, gold, white, and black, but with any other colours.
• - smooth transitions, slide show of a few tiles on home page
Should not have
• Poster
• No pictures of instruments that are not clarinet, saxophone, or flute
• Website
• Fonts in colours that can't be read on the background

```html
<!DOCTYPE html>
<html lang="en">
<head>
<meta charset="utf-8">
<title>Lanterns of Marrow Hollow — Concert Poster</title>
<link rel="stylesheet" href="https://fonts.googleapis.com/css2?family=Oswald:wght@400;600&family=Jost:wght@400;600&family=Cormorant+Garamond:wght@500&display=swap">
<style>
  :root {
    --page: #1a1816;
    --ink-deep: #050807;
    --teal-dark: #10201d;
    --teal-mid: #2c4a45;
    --teal-light: #7fa39c;
    --type: #e4e6e4;
    --type-soft: #b9bfbd;
    --rule: #8a918f;
    --gold: #c99a2e;
  }
  html, body {
    margin: 0;
    width: 1200px;
    height: 1200px;
    overflow: hidden;
    background: var(--page);
  }
  .poster {
    position: relative;
    width: 1200px;
    height: 1200px;
    overflow: hidden;
    background: var(--ink-deep);
  }
  .poster__photo {
    position: absolute;
    inset: 0;
    background:
      radial-gradient(ellipse 40% 30% at 30% 25%, rgba(127,163,156,0.35), transparent 70%),
      radial-gradient(ellipse 35% 45% at 20% 80%, rgba(70,105,98,0.55), transparent 75%),
      radial-gradient(ellipse 50% 40% at 55% 70%, rgba(44,74,69,0.5), transparent 70%),
      linear-gradient(160deg, var(--teal-dark) 0%, var(--ink-deep) 55%, var(--teal-dark) 100%);
  }
  .poster__shade {
    position: absolute;
    inset: 0;
    background: linear-gradient(200deg, rgba(5,8,7,0.95) 0%, rgba(5,8,7,0.6) 35%, transparent 60%);
  }
  .ensemble-mark {
    position: absolute;
    left: 60px;
    top: 60px;
    padding: 18px 24px;
    border: 2px solid var(--type-soft);
    font-family: "Jost", sans-serif;
    font-weight: 600;
    font-size: 18px;
    letter-spacing: 3px;
    line-height: 1.3;
    color: var(--type);
    text-transform: uppercase;
  }
  .title {
    position: absolute;
    left: 60px;
    bottom: 170px;
    margin: 0;
    font-family: "Cormorant Garamond", serif;
    font-weight: 500;
    font-size: 96px;
    line-height: 0.95;
    letter-spacing: 4px;
    color: var(--type);
    text-transform: uppercase;
  }
  .gold-dot {
    position: absolute;
    left: 70px;
    bottom: 90px;
    width: 34px;
    height: 34px;
    border-radius: 50%;
    background: var(--gold);
  }
  .schedule {
    position: absolute;
    right: 70px;
    top: 200px;
    width: 560px;
    display: grid;
    grid-template-columns: 270px 1fr;
    color: var(--type);
    font-family: "Oswald", sans-serif;
  }
  .show {
    display: flex;
    align-items: flex-end;
    gap: 14px;
    padding-bottom: 10px;
  }
  .show__day {
    font-size: 20px;
    line-height: 1.1;
    color: var(--type-soft);
    letter-spacing: 1px;
  }
  .show__date {
    font-size: 64px;
    font-weight: 600;
    line-height: 1;
  }
  .show--first {
    grid-column: 1 / 3;
    justify-content: flex-start;
    padding-left: 60px;
    border-bottom: 1px solid var(--rule);
  }
  .details {
    padding: 14px 22px 10px 0;
    border-right: 1px solid var(--rule);
    text-align: right;
  }
  .details__month {
    font-size: 50px;
    font-weight: 600;
    line-height: 1;
    margin: 0 0 12px;
  }
  .details__address {
    font-family: "Jost", sans-serif;
    font-style: normal;
    font-size: 19px;
    line-height: 1.45;
    color: var(--type-soft);
  }
  .second {
    padding: 14px 0 0 24px;
  }
  .second .show {
    border-bottom: 1px solid var(--rule);
  }
  .venue-name {
    margin-top: 24px;
    font-family: "Jost", sans-serif;
    font-weight: 600;
    font-size: 28px;
    line-height: 1;
    letter-spacing: 1px;
    color: var(--type);
    text-transform: uppercase;
  }
</style>
</head>
<body>
  <main class="poster">
    <div class="poster__photo" role="img" aria-label="Dark teal photograph of a stone staircase descending through a shadowy corridor with three thin lit strips overhead"></div>
    <div class="poster__shade"></div>

    <div class="ensemble-mark">The Windlark<br>Ensemble</div>

    <h1 class="title">Lanterns of<br>Marrow Hollow</h1>
    <span class="gold-dot"></span>

    <section class="schedule">
      <div class="show show--first">
        <span class="show__day">FR<br>20H</span>
        <span class="show__date">06.21</span>
      </div>
      <div class="details">
        <p class="details__month">JULY 2016</p>
        <address class="details__address">
          Brinmoor Concert Hall<br>
          PO Box 7315<br>
          Brinmoor NSW 2990
        </address>
      </div>
      <div class="second">
        <div class="show">
          <span class="show__day">SA<br>20H</span>
          <span class="show__date">06.22</span>
        </div>
        <div class="venue-name">Brinmoor<br>Concert<br>Hall</div>
      </div>
    </section>
  </main>
</body>
</html>
```